GreenHarborPeak - Double Sided Business Card

We are looking for design options or our business cards. We are a Business Solutions and HR solutions Provider - the theme is business, for this card.

Our brand colours are represented within our logo.

Details needed to be put on the front of the business card are:

Employees name: [Sample Name]
Role: [Sample Role]

Address: Suite 4 - Level 3/48 Lindqvist Avenue Harrowfield NSW 2261
M: 0000 000 000
P: 1300 482 917
F: 1300 482 935
E: sample@greenharborpeak.com.au
www.greenharborpeak.com.au

Reason: Hello, could we please increase our deadline by 5 days. Thanking you, Tamsin

Target Market(s)

Business Owners, also Candidates looking for Employment

Industry/Entity Type

Business

Contact Information for Business Card

Role: [Sample Role]

M: 0000 000 000
P: 1300 482 917
F: 1300 482 935

Font styles to use
Sans Serif

Colors
3276b5
3176b5
0455a3
85abd2
cfdeed
ffffff
000000
1b1b1b
757575

Requirements
Must have
• Details needed to be put on the front of the business card are:
• Employees name: [Sample Name]
• Role: [Sample Role]
• Address: Suite 4 - Level 3/48 Lindqvist Avenue Harrowfield NSW 2261
• M: 0000 000 000
• P: 1300 482 917
• F: 1300 482 935
• E: sample@greenharborpeak.com.au
• www.greenharborpeak.com.au
Nice to have
• Simplicity, clean and professional.

```html
<!DOCTYPE html>
<html lang="en">
<head>
<meta charset="utf-8">
<title>GreenHarborPeak – Business Card</title>
<link rel="stylesheet" href="https://fonts.googleapis.com/css2?family=Lato:wght@400;700;900&display=swap">
<style>
  :root {
    --brand-blue: #0455a3;
    --accent-blue: #3276b5;
    --navy: #0f2a4a;
    --ink: #1b1b1b;
    --muted: #757575;
    --paper: #ffffff;
    --stage: #e9ecef;
  }
  * { box-sizing: border-box; margin: 0; padding: 0; }
  html, body { width: 1200px; height: 780px; overflow: hidden; }
  body {
    background: var(--stage);
    font-family: "Lato", Arial, sans-serif;
    position: relative;
  }
  .card {
    position: absolute;
    width: 520px;
    height: 297px;
    box-shadow: 0 6px 18px rgba(0,0,0,0.18);
    overflow: hidden;
  }
  .card--front { left: 50px; top: 110px; background: var(--paper); }
  .card--back  { left: 630px; top: 370px; background: var(--navy); color: var(--paper); }

  .brand { display: flex; flex-direction: column; align-items: flex-start; }
  .brand__row { display: flex; align-items: center; gap: 8px; }
  .brand__mark { width: 14px; height: 14px; background: currentColor; }
  .brand__name { font-weight: 900; font-size: 22px; letter-spacing: 0.5px; white-space: nowrap; }
  .brand__rule { width: 100%; height: 1px; background: currentColor; opacity: .6; margin-top: 5px; }
  .brand__tagline { font-size: 7.5px; font-weight: 700; margin-top: 3px; white-space: nowrap; }

  .card--front .brand { position: absolute; left: 150px; top: 34px; color: var(--brand-blue); }
  .card--front .brand__tagline { color: var(--ink); }

  .person { position: absolute; left: 40px; top: 118px; }
  .person__name { font-weight: 900; font-size: 17px; color: var(--navy); letter-spacing: .3px; }
  .person__role { font-size: 12px; color: var(--accent-blue); margin-top: 1px; }

  .contact { position: absolute; left: 40px; top: 168px; font-size: 11.5px; line-height: 1.55; color: var(--navy); white-space: nowrap; }
  .contact__label { color: var(--accent-blue); font-weight: 700; }
  .contact__sep { color: var(--accent-blue); margin: 0 3px; }

  .card--back .brand { position: absolute; right: 40px; top: 110px; color: var(--paper); }
  .card--back .brand__tagline { color: var(--paper); }
  .web { position: absolute; right: 40px; bottom: 34px; font-size: 14px; letter-spacing: .3px; }
</style>
</head>
<body>
  <section class="card card--front" aria-label="Business card front">
    <div class="brand">
      <div class="brand__row">
        <span class="brand__mark"></span>
        <span class="brand__name">GreenHarborPeak</span>
      </div>
      <div class="brand__rule"></div>
      <div class="brand__tagline">Guiding small and mid-sized firms toward lasting growth</div>
    </div>

    <div class="person">
      <div class="person__name">MARCUS ELLERY</div>
      <div class="person__role">Manager</div>
    </div>

    <div class="contact">
      <div>Suite 4 - Level 3/48 Lindqvist Avenue</div>
      <div>Harrowfield NSW 2261</div>
      <div><span class="contact__label">C:</span> 0000 000 000<span class="contact__sep">|</span><span class="contact__label">P:</span> 1300 482 917<span class="contact__sep">|</span><span class="contact__label">F:</span> 1300 482 935</div>
      <div><span class="contact__label">E:</span> sample@greenharborpeak.com.au</div>
    </div>
  </section>

  <section class="card card--back" aria-label="Business card back">
    <div class="brand">
      <div class="brand__row">
        <span class="brand__mark"></span>
        <span class="brand__name">GreenHarborPeak</span>
      </div>
      <div class="brand__rule"></div>
      <div class="brand__tagline">Guiding small and mid-sized firms toward lasting growth</div>
    </div>
    <div class="web">www.greenharborpeak.com.au</div>
  </section>
</body>
</html>
```